Business Card Design Project

business cards to match the logo design reference 1970674
specific details to be provided asap - message to follow
hello - thank you for the logo design (reference 1970674) which we are very happy with. In terms of business cards you presented a couple of options ie blue front/white back and then the reverse. Can we start with the white front version but change the text details to black font?
Actual details are as follows;
Dorian Plimsoll
Managing Director
e dorianplimsoll@kestrowe.com.au
t +61 2 5550 1937
m +61 400 555 219
Suite 712, Level 7, 48 Thornbury Rd
Sydney, NSW 2000, Australia
www.kestrowe.com.au

```html
<!DOCTYPE html>
<html lang="en">
<head>
<meta charset="utf-8">
<title>Kestrowe Business Cards</title>
<link rel="stylesheet" href="https://fonts.googleapis.com/css2?family=Open+Sans:wght@400;600;700&display=swap">
<style>
  :root {
    --brand-blue: #1f72ba;
    --accent-blue: #2a7fc4;
    --soft-blue: #a9cdee;
    --ink: #111111;
    --paper: #ffffff;
    --stage: #d6d7d9;
    --edge-shadow: #1a1a1a;
  }
  * { margin: 0; padding: 0; box-sizing: border-box; }
  html, body { width: 1200px; height: 650px; overflow: hidden; }
  body {
    position: relative;
    background: var(--stage);
    font-family: "Open Sans", Arial, sans-serif;
    color: var(--ink);
  }
  .card { position: absolute; }

  .card-front {
    left: 0; top: 165px; width: 587px; height: 347px;
    background: var(--brand-blue);
    box-shadow: 0 5px 0 var(--edge-shadow);
  }
  .brand-mark {
    position: absolute; left: 82px; top: 252px;
    width: 100px; height: 100px; border-radius: 50%;
    background: var(--paper);
  }
  .brand-name {
    position: absolute; left: 222px; top: 282px;
    font-size: 58px; font-weight: 700; line-height: 1;
    font-variant: small-caps; letter-spacing: 1px;
    color: var(--paper);
  }
  .website {
    position: absolute; left: 0; width: 587px; top: 464px;
    text-align: center; font-size: 19px; color: var(--paper);
  }

  .card-back {
    left: 615px; top: 165px; width: 585px; height: 350px;
    background: var(--paper);
  }
  .person-name {
    position: absolute; left: 42px; top: 30px;
    font-size: 42px; font-weight: 400; line-height: 1.1;
    font-variant: small-caps; letter-spacing: 1px;
  }
  .person-title {
    position: absolute; left: 42px; top: 76px;
    font-size: 22px; line-height: 1.1;
    font-variant: small-caps; letter-spacing: 1px;
  }
  .contact-list {
    position: absolute; left: 38px; top: 148px;
    list-style: none; font-size: 16px; line-height: 25px;
  }
  .contact-label {
    display: inline-block; width: 34px; text-align: center;
    color: var(--accent-blue);
  }
  .address {
    position: absolute; left: 42px; top: 268px;
    font-size: 16px; line-height: 22px; font-style: normal;
  }
  .back-decoration {
    position: absolute; left: 380px; top: 70px;
    width: 180px; height: 215px; border-radius: 50%;
    background: var(--soft-blue); opacity: 0.45;
  }
</style>
</head>
<body>
  <section class="card card-front">
    <div class="brand-mark" style="left:82px; top:87px;"></div>
    <div class="brand-name" style="top:117px;">Kestrowe</div>
    <div class="website" style="top:299px;">www.kestrowe.com.au</div>
  </section>

  <section class="card card-back">
    <h1 class="person-name">Dorian Plimsoll</h1>
    <p class="person-title">Managing Director</p>
    <ul class="contact-list">
      <li><span class="contact-label">E</span>dorianplimsoll@kestrowe.com.au</li>
      <li><span class="contact-label">T</span>+61 2 5550 1937</li>
      <li><span class="contact-label">M</span>+61 400 555 219</li>
    </ul>
    <address class="address">
      Suite 712, Level 7, 48 Thornbury Rd<br>
      Sydney, NSW 2000, Australia
    </address>
    <div class="back-decoration" role="img" aria-label="Brand decoration area"></div>
  </section>
</body>
</html>
```